TrivoSuite – Veloura Flyer for Plexora (Harwick Travel Corporation)

Overview
Harwick Travel Corporation is launching a series of branded flyers to highlight the features and benefits of our TrivoSuite platform — our all-in-one corporate travel technology suite.
This first flyer will spotlight Veloura, our risk management and traveller safety solution, and will be published on Plexora as part of a digital awareness campaign.
⸻
Objective
Create a striking, professional, and modern flyer that communicates how Veloura enhances the TrivoSuite platform by ensuring traveller safety, communication, and real-time updates.
The design should feel premium, contemporary, and aligned with Harwick Travel’s luxury corporate identity.
⸻
Target Audience
• Corporate clients and travel decision-makers
• Travel managers, procurement teams, and executive assistants
• Existing Harwick Travel corporate partners on Plexora
⸻
Key Message
Veloura – Your travellers’ safety, visibility, and communication, all in one place.
Part of TrivoSuite, Harwick Travel’s integrated corporate travel platform.
⸻
Core Features to Highlight
• 24/7 real-time risk alerts
• Instant traveller identification and tracking by location or timeframe
• Two-way communication between traveller and company
• Integrated with travel itineraries for seamless care
• Supports duty-of-care compliance for corporate travel policies
⸻
Tone & Style
• Sophisticated, trusted, and innovative
• Clean lines, premium feel, and minimal clutter
• Should feel like a Harwick Travel-branded asset — not overly “techy”
• Imagery: travel safety, global maps, communication lines, or business travellers in motion
⸻
Design Direction
• Brand: Use Harwick Travel brand colours (gold, charcoal, white, navy)
• Typography: Professional, modern sans-serif fonts
• Logo: Include Harwick Travel and TrivoSuite logos (can supply if needed)
• CTA: “Discover Veloura on TrivoSuite” or “Set the Gold Standard of Corporate Travel”
• Layout: Ideal for Plexora post format (square or 4:5 vertical)
⸻
Deliverables
• Editable design file (AI / PSD / InDesign)
• Final exports for social media:
• 1080x1080 px (Plexora square)
• 1080x1350 px (Plexora portrait)
• Include space for light text overlay (for post captioning later)
⸻
Inspiration
• Style similar to luxury tech or premium corporate innovation brands
• Feel: clean, high-contrast, aspirational, minimal

```html
<!DOCTYPE html>
<html lang="en">
<head>
<meta charset="utf-8">
<title>Veloura – Harwick Travel Corporation</title>
<link rel="stylesheet" href="https://fonts.googleapis.com/css2?family=Montserrat:wght@500;600;700&display=swap">
<style>
  :root {
    --navy: #0d1a3f;
    --navy-deep: #071638;
    --gold: #d9a05b;
    --blue: #2790e3;
    --slate: #7b8599;
    --white: #ffffff;
    --mist: #c9cacd;
  }
  * { margin: 0; padding: 0; box-sizing: border-box; }
  html, body { width: 1200px; height: 1200px; overflow: hidden; background: var(--white); }
  body { font-family: "Montserrat", Arial, sans-serif; }
  .flyer { position: relative; width: 1200px; height: 1200px; overflow: hidden; background: var(--white); }
  .artwork { position: absolute; inset: 0; width: 1200px; height: 1200px; }

  .headline {
    position: absolute; left: 93px; top: 88px;
    font-size: 52px; line-height: 62px; font-weight: 600;
    color: var(--navy); letter-spacing: 0.2px;
  }
  .headline .brand { color: var(--gold); }

  .subline {
    position: absolute; left: 97px; top: 287px;
    border-left: 8px solid var(--blue);
    padding-left: 24px;
    font-size: 31px; line-height: 43px; font-weight: 500;
    color: var(--blue);
  }
  .subline .brand { color: var(--gold); }

  .features {
    position: absolute; left: 97px; top: 548px; width: 600px;
    list-style: none; color: var(--white);
    font-size: 27.5px; line-height: 35px; font-weight: 500;
  }
  .features li { position: relative; padding-left: 40px; margin-bottom: 14px; }
  .features li::before {
    content: ""; position: absolute; left: 0; top: 10px;
    width: 17px; height: 17px; background: var(--gold);
  }

  .company-name {
    position: absolute; left: 93px; top: 1085px;
    font-size: 30px; line-height: 40px; font-weight: 600;
    color: var(--gold);
  }

  .cta {
    position: absolute; left: 669px; top: 1034px; width: 427px; height: 62px;
    border-radius: 31px; background: var(--navy-deep);
    border: 3px solid var(--white);
    box-shadow: 4px 5px 8px rgba(0,0,0,0.35);
    display: flex; align-items: center; justify-content: center;
    font-size: 33px; font-weight: 700; color: var(--white);
  }
  .cta .brand { color: var(--gold); margin-left: 10px; }
  .cta-note {
    position: absolute; left: 669px; top: 1110px; width: 427px; text-align: center;
    font-size: 31px; font-weight: 500; color: var(--navy-deep);
  }
  .cta-note .platform { color: var(--blue); font-size: 33px; }
</style>
</head>
<body>
<main class="flyer">
  <svg class="artwork" viewBox="0 0 1546 1546" xmlns="http://www.w3.org/2000/svg">
    <defs>
      <radialGradient id="sky-tone" cx="1" cy="0" r="0.8">
        <stop offset="0" stop-color="#c6c7ca"/>
        <stop offset="0.55" stop-color="#e6e7e8"/>
        <stop offset="1" stop-color="#ffffff"/>
      </radialGradient>
      <linearGradient id="cabin-tone" x1="0" y1="0" x2="1" y2="1">
        <stop offset="0" stop-color="#2c4670"/>
        <stop offset="0.5" stop-color="#10204a"/>
        <stop offset="1" stop-color="#0a1a3d"/>
      </linearGradient>
      <radialGradient id="portrait-tone" cx="0.5" cy="0.45" r="0.6">
        <stop offset="0" stop-color="#d9c6b0"/>
        <stop offset="0.55" stop-color="#b07540"/>
        <stop offset="1" stop-color="#5a2f14"/>
      </radialGradient>
      <clipPath id="navy-clip">
        <path d="M0,518 C360,535 660,620 880,760 L1085,1135 C860,1280 500,1350 0,1350 Z"/>
      </clipPath>
    </defs>

    <rect class="sky-photo" x="0" y="0" width="1546" height="1546" fill="url(#sky-tone)" role="img" aria-label="Aircraft wing above the clouds, seen from a window"/>

    <path class="gold-sweep" d="M0,483 C380,498 700,590 905,745 L1095,1130 C860,1300 500,1372 0,1360 Z" fill="var(--gold)"/>
    <path class="navy-panel" d="M0,518 C360,535 660,620 880,760 L1085,1135 C860,1280 500,1350 0,1350 Z" fill="url(#cabin-tone)" role="img" aria-label="Dim aircraft cabin window with a traveller's hand"/>
    <circle class="slate-ring" cx="1190" cy="835" r="342" fill="var(--slate)" clip-path="url(#navy-clip)"/>
    <circle cx="1190" cy="835" r="318" fill="var(--white)"/>
    <circle class="gold-ring" cx="1190" cy="835" r="298" fill="none" stroke="var(--gold)" stroke-width="11"/>
    <circle class="portrait" cx="1190" cy="835" r="252" fill="url(#portrait-tone)" role="img" aria-label="Businesswoman in a light suit on a phone call in an airport"/>
  </svg>

  <h1 class="headline"><span class="brand">Veloura –</span> Your travellers’ safety,<br>visibility, and communication,<br>all in one place.</h1>

  <p class="subline">Part of <span class="brand">TrivoSuite,</span> Harwick Travel’s<br>integrated corporate travel platform.</p>

  <ul class="features">
    <li>24/7 real-time risk alerts</li>
    <li>Instant traveller identification and tracking by location or timeframe</li>
    <li>Two-way communication between traveller and company</li>
    <li>Integrated with travel itineraries for seamless care</li>
    <li>Supports duty-of-care compliance for corporate travel policies</li>
  </ul>

  <p class="company-name">Harwick Travel Corporation</p>

  <a class="cta">Discover<span class="brand">Veloura</span></a>
  <p class="cta-note">on <span class="platform">TrivoSuite</span></p>
</main>
</body>
</html>
```